Quillmoor Tandem Partners needs an email sign off and professional power point template

Newly formed company and we require:1. graphic email signature on our email , and2.a professional powerpoint template (title page and sub pages) and revamp of the attached powerpoint presentation I have uploaded our business car design (logo and contact details ) and a current powerpoint template we are currently working with. Also a brief of how we operateOur mantra is Discover, Develop, Deliver.

Target Market(s)

multinationals and mid size SME's requiring help to grown new markets or geographies for their business.

Colors
000000

Requirements
Must have
• the mantra..our phases of engagement around assisting clients is:
• 1. Discover
• 2. Develop
• 3. Deliver
Nice to have
• we differentiate ourselves form consultant by actually executing the plan for them (i.e. is the delivery phase)

```html
<!DOCTYPE html>
<html lang="en">
<head>
<meta charset="utf-8">
<title>Quillmoor Tandem Partners — Email Signature</title>
<link href="https://fonts.googleapis.com/css2?family=Montserrat:wght@400;500;600&display=swap" rel="stylesheet">
<style>
  :root {
    --page-bg: #f4f5f7;
    --banner-navy: #022a3d;
    --accent-blue: #1a8fc0;
    --slate-blue: #33597a;
    --steel-blue: #3b6880;
    --text-white: #ffffff;
  }
  * { margin: 0; padding: 0; box-sizing: border-box; }
  html, body {
    width: 1200px;
    height: 1199px;
    overflow: hidden;
    background: var(--page-bg);
    font-family: "Montserrat", sans-serif;
  }
  .signature {
    position: absolute;
    left: 191px;
    top: 449px;
    width: 818px;
    height: 215px;
    background: var(--banner-navy);
    overflow: hidden;
  }
  .scenery {
    position: absolute;
    bottom: 0;
  }
  .scenery--left {
    left: 0;
    width: 154px;
    height: 114px;
    background: linear-gradient(180deg, rgba(26,143,192,0) 0%, var(--slate-blue) 35%, var(--accent-blue) 100%);
  }
  .scenery--right {
    left: 546px;
    width: 272px;
    height: 188px;
    background: linear-gradient(180deg, rgba(59,104,128,0) 0%, var(--steel-blue) 30%, var(--slate-blue) 70%, var(--accent-blue) 100%);
  }
  .brand {
    position: absolute;
    left: 184px;
    top: 44px;
    width: 80px;
    height: 126px;
    display: flex;
    flex-direction: column;
    align-items: center;
    justify-content: center;
    gap: 8px;
  }
  .brand__square {
    width: 14px;
    height: 14px;
    background: var(--accent-blue);
  }
  .brand__name {
    color: var(--text-white);
    font-weight: 600;
    font-size: 10px;
    line-height: 1.35;
    letter-spacing: 0.06em;
    text-align: center;
    text-transform: uppercase;
  }
  .person {
    position: absolute;
    left: 330px;
    top: 48px;
  }
  .person__name {
    color: var(--accent-blue);
    font-weight: 500;
    font-size: 18px;
    letter-spacing: 0.04em;
    text-transform: uppercase;
    line-height: 1;
  }
  .person__role {
    margin-top: 7px;
    color: var(--text-white);
    font-weight: 500;
    font-size: 13px;
    letter-spacing: 0.03em;
    text-transform: uppercase;
    line-height: 1;
  }
  .contacts {
    list-style: none;
    margin-top: 24px;
  }
  .contacts__item {
    display: flex;
    align-items: center;
    height: 21px;
    color: var(--text-white);
    font-size: 12.5px;
    font-weight: 400;
  }
  .contacts__icon {
    width: 11px;
    height: 11px;
    margin-right: 13px;
    flex: none;
  }
</style>
</head>
<body>
  <section class="signature">
    <div class="scenery scenery--left" role="img" aria-label="Flat blue mountain range illustration"></div>
    <div class="scenery scenery--right" role="img" aria-label="Flat blue mountain peaks illustration"></div>

    <div class="brand">
      <span class="brand__square"></span>
      <span class="brand__name">Quillmoor<br>Tandem<br>Partners</span>
    </div>

    <div class="person">
      <p class="person__name">Rowan&nbsp; Ellery</p>
      <p class="person__role">Principal</p>
      <ul class="contacts">
        <li class="contacts__item">
          <svg class="contacts__icon" viewBox="0 0 12 12"><path d="M3 1 L5 3.5 L4 5 Q5 7 7 8 L8.5 7 L11 9 L9.5 11 Q5 10.5 1 3 Z" fill="var(--accent-blue)"/></svg>
          555-218-4307
        </li>
        <li class="contacts__item">
          <svg class="contacts__icon" viewBox="0 0 12 12"><rect x="0.5" y="2.5" width="11" height="7.5" fill="var(--accent-blue)"/><path d="M0.8 2.8 L6 6.8 L11.2 2.8" fill="none" stroke="var(--banner-navy)" stroke-width="1"/></svg>
          rowan.ellery@quillmoor.ca
        </li>
        <li class="contacts__item">
          <svg class="contacts__icon" viewBox="0 0 12 12" fill="none" stroke="var(--accent-blue)" stroke-width="1.1"><circle cx="6" cy="6" r="5"/><ellipse cx="6" cy="6" rx="2.2" ry="5"/><path d="M1 6 H11 M2 3.3 H10 M2 8.7 H10"/></svg>
          www.quillmoor.ca
        </li>
      </ul>
    </div>
  </section>
</body>
</html>
```